Schnapsbrennerei sucht neue Etiketten
Zielgruppe
Wir sind eine örtliche Schnapsbrennerei, die inzwischen seit ein paar Jahren einen eigenen Kundenstamm aufgebaut hat. Nun werden wir im nächsten Jahr einen neuen Verkaufsraum bauen. Aus diesem Grund wollen wir unsere Etiketten komplett überarbeiten.
Ein neues Logo habe ich bereits designen lassen. Diese finden Sie unten im Dokumententenupload. Wir legen viel Wert auf eine sehr hohe Qualität, welche sich sowohl in unserem Logo als auch den Etiketten Wiederspiegeln soll.
Unsere Kundschaft ist hauptsächlich Ü35 und legt viel Wert auf hochwertige Produkte.
Aufgabenstellung
Eines direkt vorne weg: Da wir unsere komplette Produktpalette neu gestalten wollen würde ich Sie bitten, der Einfachheit halber zuerst nur ein Schnapsetikett (z.B. Zwetschge oder Willi), ein Likör Etikett und ein Etikett für unseren Whiskey zu erstellen.
Darüber hinaus bitte ich Sie auch ein Design für unseren neuen Gin und einen Aquavit, welcher im Herbst auf den Markt kommen soll zu designen. Im Anschluss daran, werde ich in der Zusammenarbeit mit Ihnen die Etiketten optimieren wollen.
Sobald ein 'Grundetikett' entstanden ist, sollen dann auch die anderen Schnäpse und Liköre in dem gleichen Stil erstellt werden. Explizit möchte ich daraufhin weisen, dass sowohl die Whiskeys als auch der Gin und der Aquavit nicht zwangsläufig das gleiche 'Grundetikett' wie der Schnaps und der Likör haben sollen. Ist bei unseren aktuellen Etiketten auch nicht der Fall. Sehen Sie in den Bildern unten.
Wir verkaufen unseren Schnaps und Likör in 3 unterschieldichen Größen 0,2; 0,5 und 1,0 Liter. Wir verwenden für die 0,2 und 0,5 die Flasche Tessa. Das Etikett der 0,5er Flasche soll in etwa 65x120-130 mm sein. Hier sind wir allerdings variabel.
Dieses entstandene Etikett soll dann auf die anderen Flaschen entsprechend angepasst werden.
Sie finden im Dokumentenupload unsere aktuellen Etiketten und das Logo, welches eingebaut werden soll. Auch ein Etikett von einem örtlichen Weingut, welches mir vom Aufbau und der Unterteilung sehr gut gefällt, werde ich mit anhängen. Allerdings ist dieses Bild sehr unscharf. Wie gesagt es geht hierbei hauptsächlich um die Einteilung mit den oberen und den unteren 'Rahmen'.
Auch unsere Preisliste finden Sie Anhang, wobei diese noch in der Rohform ist und das Obst so nicht verwendet wird, aber hier sind die meisten Produkte drauf.
Das Logo gibt es in verschiedenen Farben. Gerne dürfen Sie für die unterschiedlichen Produkte auch unterschiedliche Farben nutzen.
Was ich mir persönlich g..

```html
<!DOCTYPE html>
<html lang="de">
<head>
<meta charset="utf-8">
<title>Haldner's Zwetchge – Etikett</title>
<link href="https://fonts.googleapis.com/css2?family=Playfair+Display:wght@400;500&family=Oswald:wght@400&family=Montserrat:wght@500;700&display=swap" rel="stylesheet">
<style>
  :root {
    --backdrop: #e4e4e4;
    --band-dark: #3b3b3b;
    --panel-cream: #f1efea;
    --gold: #b8923a;
    --gold-line: #a8843a;
    --ink: #3e3c48;
    --band-text: #e8e6e1;
    --plum: #5d5a6b;
  }
  * { margin: 0; padding: 0; box-sizing: border-box; }
  html, body { width: 1180px; height: 1200px; overflow: hidden; }
  body { background: var(--backdrop); position: relative; }

  .label {
    position: absolute; left: 310px; top: 65px;
    width: 560px; height: 1070px;
    background: var(--band-dark);
  }
  .label__frame {
    position: absolute; left: 23px; top: 20px; right: 23px; bottom: 28px;
    border: 1.5px solid var(--gold-line);
    pointer-events: none; z-index: 3;
  }
  .band-top {
    position: absolute; left: 0; top: 0; width: 100%; height: 262px;
    display: flex; flex-direction: column; align-items: center; justify-content: flex-end;
    padding-bottom: 30px;
  }
  .brand-mark {
    display: flex; flex-direction: column; align-items: center; gap: 10px;
  }
  .brand-mark__dot {
    width: 54px; height: 54px; border-radius: 50%;
    border: 2px solid var(--band-text); margin-bottom: 18px;
  }
  .brand-mark__name {
    font-family: "Montserrat", sans-serif; font-weight: 700;
    font-size: 25px; letter-spacing: 5px; color: var(--band-text);
  }
  .brand-mark__sub {
    font-family: "Montserrat", sans-serif; font-weight: 500;
    font-size: 8px; letter-spacing: 4px; color: var(--band-text);
  }

  .panel {
    position: absolute; left: 0; top: 262px; width: 100%; height: 576px;
    background: var(--panel-cream);
  }
  .product-title {
    position: absolute; left: 0; width: 100%; top: 34px; text-align: center;
    font-family: "Playfair Display", serif; font-weight: 400;
    font-size: 60px; color: var(--gold); line-height: 1; letter-spacing: 1px;
    transform: scaleX(0.82);
  }
  .product-variety {
    position: absolute; left: 0; width: 100%; top: 116px; text-align: center;
    font-family: "Playfair Display", serif; font-weight: 500;
    font-size: 38px; color: var(--gold); line-height: 1; letter-spacing: 3px;
    transform: scaleX(0.75);
  }
  .fruit-art {
    position: absolute; left: 129px; top: 182px; width: 310px; height: 268px;
  }
  .tagline {
    position: absolute; left: 0; width: 100%; top: 482px; text-align: center;
    font-family: "Oswald", sans-serif; font-size: 18px; color: var(--ink);
    letter-spacing: 0.5px; transform: scaleX(0.85);
  }
  .specs {
    position: absolute; left: 46px; right: 46px; top: 536px;
    display: flex; justify-content: space-between;
    font-family: "Montserrat", sans-serif; font-weight: 500;
    font-size: 19px; color: var(--ink); letter-spacing: 1px;
  }

  .band-bottom {
    position: absolute; left: 0; top: 838px; width: 100%; height: 232px;
    text-align: center; color: var(--band-text);
    font-family: "Montserrat", sans-serif; font-weight: 500;
  }
  .producer {
    margin-top: 38px; font-size: 16px; line-height: 20px; letter-spacing: 2px;
    font-style: normal;
  }
  .batch {
    margin-top: 30px; font-size: 12px; letter-spacing: 1px;
  }
</style>
</head>
<body>
  <article class="label">
    <div class="label__frame"></div>

    <header class="band-top">
      <div class="brand-mark">
        <span class="brand-mark__dot"></span>
        <span class="brand-mark__name">HALDNER'S</span>
        <span class="brand-mark__sub">LANDBRENNEREI</span>
      </div>
    </header>

    <section class="panel">
      <h1 class="product-title">HALDNER'S</h1>
      <h2 class="product-variety">ZWETCHGE</h2>
      <svg class="fruit-art" viewBox="0 0 310 268" role="img" aria-label="Zeichnung einer halbierten Zwetschge und einer ganzen Zwetschge mit Blatt">
        <defs>
          <radialGradient id="plumTone" cx="50%" cy="50%" r="50%">
            <stop offset="0%" stop-color="#8a8797"/>
            <stop offset="100%" stop-color="#d9d7dd"/>
          </radialGradient>
        </defs>
        <rect width="310" height="268" rx="20" fill="url(#plumTone)" opacity="0.55"/>
      </svg>
      <p class="tagline">HALDNER'S BIRNE IM HOLZFASS GEREIFT</p>
      <div class="specs">
        <span class="specs__abv">40% vol.</span>
        <span class="specs__volume">0,5 l</span>
      </div>
    </section>

    <footer class="band-bottom">
      <address class="producer">
        EDELBRÄ &amp; LIKÖRE<br>
        KONRAD HALDNER<br>
        LINDENWEG 4<br>
        D.96412 AURACH<br>
        TEL. 09512 / 4380
      </address>
      <p class="batch">1.07/06</p>
    </footer>
  </article>
</body>
</html>
```